Stylish new business card needed!

Hello everyone! I am in need of a new business card design for an alarm company here in Hurricane WV. I have all fonts, color codes and logos provided for you use! We are a young company and like the style of a clean sleek looking business card. Would like it double sided, one side holding the logo and the other with your design!
Target Market(s)
The people that are looking for the newest tech for home automation and security
Industry/Entity Type
Alarm services; Home automation
Contact Information for Business Card
Name of person; position (Sales; Installer); Phone Number (555.419.7362); Employee cell Number; Website (www.GuardedByVelm.example); Employee Email; Double sided
Look and feel
Each slider illustrates characteristics of the customer's brand and the style your logo design should communicate.

```html
<!DOCTYPE html>
<html lang="en">
<head>
<meta charset="utf-8">
<title>VELM Business Card – Front and Back</title>
<link rel="stylesheet" href="https://fonts.googleapis.com/css2?family=Lato:wght@300;400;700;900&display=swap">
<style>
  :root {
    --backdrop: #2b2e33;
    --card-white: #ffffff;
    --card-grey: #999a9c;
    --ink-grey: #8f9093;
    --text-grey: #6d6e71;
    --accent: #f58a3c;
    --line-white: #ffffff;
  }
  * { box-sizing: border-box; margin: 0; padding: 0; }
  html, body {
    width: 1200px; height: 952px; overflow: hidden;
    background: var(--backdrop);
    font-family: "Lato", Arial, sans-serif;
  }
  .sheet {
    width: 1200px; height: 952px;
    display: flex; flex-direction: column;
    align-items: center; justify-content: center; gap: 60px;
  }
  .card {
    position: relative;
    width: 620px; height: 354px;
    border-radius: 22px;
    overflow: hidden;
  }
  .card--front { background: var(--card-white); }
  .card--back { background: var(--card-grey); }

  .card__rule { position: absolute; inset: 0; width: 100%; height: 100%; }

  /* front */
  .brand-name {
    position: absolute;
    font-weight: 300;
    letter-spacing: 2px;
    line-height: 1;
  }
  .card--front .brand-name {
    left: 58px; top: 84px;
    font-size: 92px;
    color: var(--ink-grey);
  }
  .contact {
    position: absolute; left: 340px; top: 150px;
    color: var(--text-grey);
  }
  .contact__name {
    font-size: 20px; font-weight: 400; letter-spacing: 1px;
    color: var(--accent); text-transform: uppercase;
  }
  .contact__name strong { font-weight: 900; }
  .contact__role { font-size: 15px; margin-top: 2px; }
  .contact__divider {
    width: 46px; height: 2px; background: var(--accent);
    margin: 8px 0 12px;
  }
  .contact__list { list-style: none; font-size: 13px; }
  .contact__item {
    display: flex; align-items: center; gap: 9px;
    margin-bottom: 7px;
  }
  .contact__icon {
    width: 17px; height: 17px; border-radius: 3px;
    background: var(--accent);
    display: flex; align-items: center; justify-content: center;
    flex: none;
  }

  /* back */
  .back-lockup {
    position: absolute; left: 0; right: 0; top: 108px;
    text-align: center;
  }
  .card--back .brand-name {
    position: static;
    font-size: 100px; color: var(--card-white);
  }
  .back-lockup__tagline {
    margin-top: 10px;
    font-size: 11px; font-weight: 700; letter-spacing: 2px;
    color: var(--accent);
  }
</style>
</head>
<body>
<main class="sheet">

  <section class="card card--front" aria-label="Card front">
    <svg class="card__rule" viewBox="0 0 620 354" aria-hidden="true">
      <polyline points="0,52 6,52 6,52" fill="none"/>
      <line x1="0" y1="283" x2="200" y2="283" stroke="#8f9093" stroke-width="2.5"/>
      <line x1="200" y1="283" x2="208" y2="291" stroke="#8f9093" stroke-width="2.5"/>
      <line x1="208" y1="291" x2="620" y2="291" stroke="#f58a3c" stroke-width="4"/>
    </svg>

    <div class="brand-name">VELM</div>

    <div class="contact">
      <h1 class="contact__name">Daniel R. <strong>Ashford</strong></h1>
      <p class="contact__role">Managing Director</p>
      <div class="contact__divider"></div>
      <ul class="contact__list">
        <li class="contact__item">
          <span class="contact__icon">
            <svg width="11" height="11" viewBox="0 0 24 24" aria-hidden="true"><path fill="#fff" d="M6.6 10.8a15.1 15.1 0 0 0 6.6 6.6l2.2-2.2a1 1 0 0 1 1-.25 11.4 11.4 0 0 0 3.6.57 1 1 0 0 1 1 1V20a1 1 0 0 1-1 1A17 17 0 0 1 3 4a1 1 0 0 1 1-1h3.5a1 1 0 0 1 1 1c0 1.25.2 2.45.57 3.57a1 1 0 0 1-.25 1z"/></svg>
          </span>555.419.7362
        </li>
        <li class="contact__item">
          <span class="contact__icon">
            <svg width="11" height="11" viewBox="0 0 24 24" aria-hidden="true"><rect x="2" y="5" width="20" height="14" rx="1.5" fill="none" stroke="#fff" stroke-width="2"/><path d="M2 6l10 7 10-7" fill="none" stroke="#fff" stroke-width="2"/></svg>
          </span>hello@guardedbyvelm.example
        </li>
        <li class="contact__item">
          <span class="contact__icon">
            <svg width="11" height="11" viewBox="0 0 24 24" aria-hidden="true"><path fill="#fff" d="M12 2a7 7 0 0 0-7 7c0 5 7 13 7 13s7-8 7-13a7 7 0 0 0-7-7zm0 9.5A2.5 2.5 0 1 1 12 6.5a2.5 2.5 0 0 1 0 5z"/></svg>
          </span>www.GuardedByVelm.example
        </li>
      </ul>
    </div>
  </section>

  <section class="card card--back" aria-label="Card back">
    <svg class="card__rule" viewBox="0 0 620 354" aria-hidden="true">
      <line x1="0" y1="283" x2="200" y2="283" stroke="#ffffff" stroke-width="2.5"/>
      <line x1="200" y1="283" x2="208" y2="291" stroke="#ffffff" stroke-width="2.5"/>
      <line x1="208" y1="291" x2="620" y2="291" stroke="#f58a3c" stroke-width="4"/>
    </svg>

    <div class="back-lockup">
      <div class="brand-name">VELM</div>
      <p class="back-lockup__tagline">AUTOMATION AND SECURITY SERVICES</p>
    </div>
  </section>

</main>
</body>
</html>
```